依頼詳細
ポスティング形式での営業となりますので、
一目見て目に付くようなチラシデザインで
あれば、多少デザインに派手さが入っても
良いとは思っています。

「本当に和室のままでイイですか?」
というアラートの様なタイトルがどれだけ
目を引くかに重点を置いて考えています。

また、何故和室を洋室に変えた方がイイと
いう根拠につきましては、
・畳の経年寿命の早さとメンテナンス&交換をしてない畳のアレルギー等の促進を
進めるという情報をわかりやすくアラートをお伝えした文章が欲しいです。(ハウスダスト・ダニ・花粉)

価格帯の記載
・マンションアパートタイプであれば
1畳単価50000円〜
・戸建てタイプの場合い1畳単価60000円〜
押し入れのクローゼット化 10000円〜

室内の物の移動等も含める作業は別途
お見積もりとの別記載も入れて欲しい。

和室〜洋室に変えた際のビフォーアフターの
写真等も添付したいです。
記載項目
翠昇株式会社 03-6812-3097
HP https://suishoweb.ne.jp/
キャッチコピー「和室のままで本当にイイですか?」
サイズ
A4
ページ数
両面
希望イメージ
シンプル 複雑
単色 カラフル
暗い 明るい
日常 高級
遊び心 厳粛
未来的 伝統的
女性的 男性的
希望する色
青系
納品ファイル
• 高解像度JPG (.jpg)
• PNG形式 (.png)
補足説明
デザイン 文章 画像についても提案があれば都度頂きたい。
■ 選んだ理由

シンプルで有りながらも、ディテールの部分の丁寧さがスゴく見やすく思えました。文章につきましても
拙い説明にも関わらず、しっかり拾い上げて頂けたのが1番決め手となりました。本当にありがとうございます。

■ 提案者全員のお礼・コメント

この度は沢山のご提案頂きありがとうございました。
タスクフォルンを使ったのは初めてで、色々分からず皆様に失礼が有りましたらここでお詫びさせて下さい。

とてもタスクフォルンのサービスとデザイナーの皆様の
技術に大変関心を持ちました。今後も色んな事で
運用したいと思っておりますので、また機会が
ございましたら何卒よろしくお願い致します。

この度は誠に有難うございました。

```html
<!DOCTYPE html>
<html lang="ja">
<head>
<meta charset="utf-8">
<title>和室の洋室化リフォームのご案内</title>
<link rel="stylesheet" href="https://fonts.googleapis.com/css2?family=Shippori+Mincho:wght@500;700&family=Noto+Sans+JP:wght@400;700&display=swap">
<style>
  :root {
    --paper: #ffffff;
    --ink: #1c1c1c;
    --accent-blue: #1f4f9e;
    --band-tan: #d8c59b;
    --band-ink: #2b2418;
    --photo-light: #ece5d6;
    --photo-mid: #c9b792;
    --photo-floor: #b9a470;
  }
  * { box-sizing: border-box; margin: 0; padding: 0; }
  html, body { width: 879px; height: 1200px; overflow: hidden; background: var(--paper); }
  .flyer { position: relative; width: 879px; height: 1200px; background: var(--paper); color: var(--ink);
    font-family: "Shippori Mincho", serif; overflow: hidden; }

  .vertical { writing-mode: vertical-rl; text-orientation: mixed; position: absolute; white-space: nowrap; }

  .lead-tag { top: 44px; right: 40px; font-family: "Noto Sans JP", sans-serif; font-weight: 700;
    font-size: 20px; letter-spacing: 0.05em; color: var(--accent-blue); }

  .headline { top: 96px; right: 106px; font-weight: 700; font-size: 72px; line-height: 1.42;
    letter-spacing: 0.03em; }
  .headline span { display: block; }

  .body-copy { top: 132px; left: 252px; font-family: "Noto Sans JP", sans-serif;
    font-size: 19px; line-height: 1.72; letter-spacing: 0.04em; }

  .room-photo { position: absolute; left: 30px; top: 668px; width: 470px; height: 292px;
    background: linear-gradient(180deg, var(--photo-light) 0%, #e4dac4 58%, var(--photo-mid) 74%, var(--photo-floor) 100%); }

  .site-url { position: absolute; right: 120px; top: 980px; font-family: "Noto Sans JP", sans-serif;
    font-size: 15px; letter-spacing: 0.02em; }

  .footer-band { position: absolute; left: 0; bottom: 0; width: 100%; height: 160px; background: var(--band-tan);
    color: var(--band-ink); font-family: "Noto Sans JP", sans-serif; padding: 30px 32px; }
  .company-name { font-size: 26px; font-weight: 700; letter-spacing: 0.03em; }
  .company-name .kana { font-size: 17px; }
  .company-contact { margin-top: 26px; font-size: 14px; letter-spacing: 0.02em; }
  .service-note { position: absolute; left: 380px; top: 40px; font-size: 13px; }
  .cta-pill { position: absolute; right: 28px; bottom: 30px; width: 380px; height: 44px; border-radius: 22px;
    background: var(--paper); display: flex; align-items: center; padding-left: 34px; font-size: 14px; }
  .cta-pill svg { position: absolute; right: 5px; top: 5px; }
</style>
</head>
<body>
<main class="flyer">
  <p class="vertical lead-tag">●翠昇株式会社が提案する「和室の洋室化リフォーム」のご案内です。</p>

  <h1 class="vertical headline">
    <span>和室のままで</span>
    <span>本当に、イイですか？</span>
  </h1>

  <div class="vertical body-copy">
    <p>和室が使いずらくなっていませんか？</p>
    <p>通常、畳は約三〜五年で裏返しを行い</p>
    <p>七〜八年程度で表替えを行わなくてはなりません。</p>
    <p>湿気でカビが発生する場合もあります。</p>
    <p>その他、押し入れや床の間、建具の老朽化の</p>
    <p>風通しもよくなり、使いずらさをお感じでしたら、</p>
    <p>洋室化のリフォームをご検討ください。</p>
  </div>

  <div class="room-photo" role="img" aria-label="畳敷きの和室と襖の写真"></div>

  <p class="site-url">https://suishoweb.ne.jp/</p>

  <footer class="footer-band">
    <p class="company-name">翠昇<span class="kana">(すいしょう)</span>株式会社</p>
    <p class="company-contact">〒155-0031 東京都世田谷区北沢4-18-7　TEL 03-6812-3097</p>
    <p class="service-note">畳から快適な洋室へ、暮らしに合わせた和室の改装をご提案します。</p>
    <div class="cta-pill">詳しい内容は裏面をご覧ください
      <svg width="34" height="34" viewBox="0 0 36 36" aria-hidden="true">
        <circle cx="18" cy="18" r="18" fill="#1c1c1c"/>
        <path d="M15 11 L22 18 L15 25" fill="none" stroke="#fff" stroke-width="3" stroke-linecap="round" stroke-linejoin="round"/>
      </svg>
    </div>
  </footer>
</main>
</body>
</html>
```